Disability provider requiring digital flyer to promote services

My company works within the Disability sector (QCWP registered provider), currently operating in Sydney, Australia.
I require a digital brochure which lists our services and gives potential customers a quick look into what we do with a single glance.
Undecided whether this digital flyer is to be single or double sided, happy to consult with an experienced designer in this regard.
I prefer minimalist designs (which may be an issue for someone trying to convey information, I'm not sure), and possibly someone who can work with out watercolor logo.
Services include:
-Supported Independent Living
-Specialist Disability Accommodation
-Individualised Living Options Stage 1 & 2
-Home Modifications
-Occupational Therapy
-Support Coordination Levels 1 & 2
-Short Term Accommodation - STA Respite
-Drop In Supports
-Community Access

```html
<!DOCTYPE html>
<html lang="en">
<head>
<meta charset="utf-8">
<title>Clearview Care – Services Flyer</title>
<link rel="stylesheet" href="https://fonts.googleapis.com/css2?family=Bebas+Neue&family=Playfair+Display:wght@900&display=swap">
<style>
  :root {
    --backdrop: #e4e9f1;
    --paper: #ffffff;
    --panel: #eaf0f9;
    --magenta: #c81ba8;
    --teal: #0fd6b4;
    --sun: #fcc85e;
    --ink: #3f3f44;
    --charcoal: #444446;
    --white: #ffffff;
  }
  * { box-sizing: border-box; margin: 0; padding: 0; }
  html, body { width: 1200px; height: 1200px; overflow: hidden; }
  body { background: var(--backdrop); position: relative; font-family: "Bebas Neue", "Arial Narrow", sans-serif; }

  .flyer { position: absolute; left: 204px; top: 40px; width: 792px; height: 1120px; background: var(--paper); overflow: hidden; }
  .hero-panel { position: absolute; left: 42px; top: 40px; width: 706px; height: 445px; background: var(--panel); }
  .sun-band { position: absolute; left: 0; top: 747px; width: 792px; height: 288px; background: var(--sun); }
  .services-box { position: absolute; left: 246px; top: 452px; width: 502px; height: 466px; background: var(--magenta); }

  .hero-photo { position: absolute; left: 107px; top: 47px; width: 297px; height: 405px;
    background: linear-gradient(160deg, #dfe6f2 0%, #3b4f86 45%, #2b3866 80%, #3a6fd0 100%); border-radius: 40px 40px 0 0; }

  .brand { position: absolute; right: 66px; top: 176px; display: flex; align-items: center; gap: 8px;
    font-size: 34px; color: var(--ink); letter-spacing: 1px; line-height: 1; }
  .brand-dot { width: 18px; height: 18px; border-radius: 50%; background: var(--teal); }

  .tagline { position: absolute; right: 66px; top: 236px; font-size: 19px; color: var(--ink); letter-spacing: 0.3px; }
  .motto-lead { position: absolute; right: 66px; top: 280px; font-size: 34px; color: var(--magenta); line-height: 1; }
  .motto-main { position: absolute; right: 64px; top: 316px; font-size: 72px; color: var(--teal); line-height: 1; letter-spacing: 0.5px; }

  .snapshot { position: absolute; width: 205px; border: 6px solid var(--teal); box-shadow: 0 6px 12px rgba(0,0,0,0.28); }
  .snapshot-1 { left: 52px; top: 416px; height: 148px; transform: rotate(4deg); background: linear-gradient(135deg, #e9ecef, #8fa0b8 55%, #46516a); }
  .snapshot-2 { left: 42px; top: 568px; height: 132px; transform: rotate(-9deg); background: linear-gradient(180deg, #c8d6e6 0%, #6f9a55 40%, #d66a62 75%, #c95a55); }
  .snapshot-3 { left: 46px; top: 700px; height: 132px; transform: rotate(4deg); background: linear-gradient(120deg, #3c5aa6, #4a4f5e 45%, #cfd6de); }
  .snapshot-4 { left: 42px; top: 838px; height: 130px; transform: rotate(-4deg); background: linear-gradient(120deg, #cfd4dc, #2d3348 40%, #e7e9ed 70%, #9aa2ae); }

  .services-title { position: absolute; left: 295px; top: 478px; font-family: "Playfair Display", Georgia, serif; font-weight: 900;
    font-size: 34px; color: var(--white); letter-spacing: 0.5px; }
  .service-list { position: absolute; left: 320px; top: 540px; list-style: none; }
  .service-list li { display: flex; align-items: center; gap: 8px; height: 40px; font-size: 22px; color: var(--white); }
  .service-icon { width: 28px; height: 28px; border-radius: 50%; background: var(--white); display: flex; align-items: center; justify-content: center; flex: none; }

  .about { position: absolute; right: 44px; top: 952px; width: 720px; text-align: right; font-size: 16.5px; line-height: 24px; color: var(--ink); }

  .footer-contact { position: absolute; left: 0; top: 1035px; width: 392px; height: 85px; background: var(--teal); padding: 22px 0 0 24px; }
  .footer-info { position: absolute; left: 392px; top: 1035px; width: 400px; height: 85px; background: var(--charcoal); padding: 22px 23px 0 0; text-align: right; }
  .contact-line { display: flex; align-items: center; gap: 6px; font-size: 18px; color: var(--white); height: 24px; }
  .footer-info .contact-line { justify-content: flex-end; }
  .social-box { width: 15px; height: 15px; border: 1.5px solid var(--white); border-radius: 3px; }
</style>
</head>
<body>
  <main class="flyer">
    <div class="hero-panel"></div>
    <div class="sun-band"></div>
    <div class="services-box"></div>

    <div class="hero-photo" role="img" aria-label="Photo of a smiling man standing behind a woman seated in a wheelchair"></div>

    <div class="brand"><span class="brand-dot"></span><span>Clearview Care</span></div>
    <p class="tagline">CLEARVIEW FOR AN EMPOWERED FUTURE</p>
    <p class="motto-lead">NOTHING ABOUT US</p>
    <p class="motto-main">WITHOUT US</p>

    <div class="snapshot snapshot-1" role="img" aria-label="Photo of a group of people, including a wheelchair user, chatting in an office"></div>
    <div class="snapshot snapshot-2" role="img" aria-label="Photo of a woman in a wheelchair and a child on a running track"></div>
    <div class="snapshot snapshot-3" role="img" aria-label="Photo of a man in a power wheelchair inside a bright building"></div>
    <div class="snapshot snapshot-4" role="img" aria-label="Photo of a businessman shaking hands with a woman in a wheelchair"></div>

    <h2 class="services-title">SERVICES INCLUDE:</h2>
    <ul class="service-list">
      <li><span class="service-icon"><svg width="16" height="16" viewBox="0 0 16 16" fill="none" stroke="#c81ba8" stroke-width="1.5"><path d="M2 8 L8 3 L14 8 M4 7 V13 H12 V7"/></svg></span>SUPPORTED INDEPENDENT LIVING</li>
      <li><span class="service-icon"><svg width="16" height="16" viewBox="0 0 16 16" fill="none" stroke="#c81ba8" stroke-width="1.5"><rect x="3" y="5" width="10" height="8"/><path d="M2 6 L8 2 L14 6"/></svg></span>SPECIALIST DISABILITY ACCOMMODATION</li>
      <li><span class="service-icon"><svg width="16" height="16" viewBox="0 0 16 16" fill="none" stroke="#c81ba8" stroke-width="1.5"><circle cx="8" cy="5" r="2.5"/><path d="M3 14 C3 9 13 9 13 14"/></svg></span>INDIVIDUALISED LIVING OPTIONS STAGE 1 &amp; 2</li>
      <li><span class="service-icon"><svg width="16" height="16" viewBox="0 0 16 16" fill="none" stroke="#c81ba8" stroke-width="1.5"><path d="M2 8 L8 3 L14 8 M4 7 V13 H12 V7 M7 13 V10 H9 V13"/></svg></span>HOME MODIFICATIONS</li>
      <li><span class="service-icon"><svg width="16" height="16" viewBox="0 0 16 16" fill="none" stroke="#c81ba8" stroke-width="1.5"><circle cx="5" cy="9" r="3"/><path d="M10 5 H15 M12.5 5 V13"/></svg></span>OCCUPATIONAL THERAPY</li>
      <li><span class="service-icon"><svg width="16" height="16" viewBox="0 0 16 16" fill="none" stroke="#c81ba8" stroke-width="1.5"><circle cx="5" cy="5" r="2"/><circle cx="11" cy="5" r="2"/><path d="M2 13 C2 9 14 9 14 13"/></svg></span>SUPPORT COORDINATION LEVELS 1 &amp; 2</li>
      <li><span class="service-icon"><svg width="16" height="16" viewBox="0 0 16 16" fill="none" stroke="#c81ba8" stroke-width="1.5"><circle cx="10" cy="5" r="3"/><path d="M2 12 H7 L11 10"/></svg></span>SHORT TERM ACCOMMODATION - STA RESPITE</li>
      <li><span class="service-icon"><svg width="16" height="16" viewBox="0 0 16 16" fill="none" stroke="#c81ba8" stroke-width="1.5"><path d="M8 2 C5 6 5 8 8 9 C11 8 11 6 8 2 Z M2 11 L8 14 L14 11"/></svg></span>DROP IN SUPPORTS</li>
      <li><span class="service-icon"><svg width="16" height="16" viewBox="0 0 16 16" fill="none" stroke="#c81ba8" stroke-width="1.5"><circle cx="8" cy="5" r="2"/><circle cx="3.5" cy="7" r="1.5"/><circle cx="12.5" cy="7" r="1.5"/><path d="M4 14 C4 10 12 10 12 14"/></svg></span>COMMUNITY ACCESS</li>
    </ul>

    <p class="about">CLEARVIEW CARE IS A SYDNEY BASED DISABILITY SUPPORT SERVICES<br>PROVIDER. FOCUSING ON INTELLECTUAL, PHYSICAL &amp; SENSORY DISABILITIES INCLUDING MENTAL<br>HEALTH WITHIN THE GREATER SYDNEY REGION, WE STRIVE TO ASSIST OUR PARTICIPANTS IN LEADING AN INDEPENDENT AND FULFILLING LIFE.</p>

    <footer>
      <div class="footer-contact">
        <p class="contact-line"><svg width="16" height="16" viewBox="0 0 16 16"><rect x="0.5" y="0.5" width="15" height="15" rx="3" fill="#fff"/><path d="M5 3 L7 5.5 L6 7 C7 9 8 10 9.5 10.5 L11 9.5 L13 11.5 L11.5 13 C7 12.5 4 9 3.5 4.5 Z" fill="#0fd6b4"/></svg>+61 0491 570 156</p>
        <p class="contact-line"><svg width="20" height="14" viewBox="0 0 20 14" fill="none" stroke="#fff" stroke-width="1.3"><rect x="1" y="1" width="18" height="12"/><path d="M1 1 L10 8 L19 1 M1 13 L8 6.5 M19 13 L12 6.5"/></svg>HELLO@CLEARVIEWCARE.COM.AU</p>
      </div>
      <div class="footer-info">
        <p class="contact-line">FOLLOW US : <span class="social-box"></span><span class="social-box"></span><span class="social-box"></span></p>
        <p class="contact-line">OPERATING HOURS: 9AM TO 5PM MONDAY - FRIDAY <svg width="16" height="16" viewBox="0 0 16 16" fill="none" stroke="#fff" stroke-width="1.3"><circle cx="8" cy="8" r="7"/><path d="M8 4 V8 L5.5 10"/></svg></p>
      </div>
    </footer>
  </main>
</body>
</html>
```